Construction company focused on concrete and shed construction.

We need to update our current business card for brindlebuilds.com.au we would like an eye catching design with blue, grey and white incorporating our current logo.
Our company started off in concreting and due to varying factors we have expanded to include shed construction as well.
This has led to our current Logo looking a little out of place and somehow need to use the card to bring in the shed construction side of the business while not having to change current concrete look "BRINDLE" logo as we already have this incorporated into our company clothing and are not willing to change this yet.
Photo image attached for inspiration/ visual reference of type of work, not to be used on final design.
Please no cheesy designs of men in hard hats and tools
Final design should demonstrate a modern and service focused company.

Target Market(s)

Farmers, Business owners, Developers, Architects, Commercial project delivery

Industry/Entity Type

Construction Company

Contact Information for Business Card

Brindle Builds.
7c Harcourt st
Kingsmeadow Tas
03 62918730

Font styles to use
Other font styles liked:
• see font in logo

Colors
3176b5
b2b2b2

Requirements
Must have
• Easy to read font,
• good contrast between back ground and writing
Nice to have
• Modern and corporate look with a fun but professional image.
Should not have
• Comic images or shadow images of tools/ people.

```html
<!DOCTYPE html>
<html lang="en">
<head>
<meta charset="utf-8">
<title>Brindle Builds – Business Card</title>
<link rel="stylesheet" href="https://fonts.googleapis.com/css2?family=Oswald:wght@500;600&family=Montserrat:wght@400;500&display=swap">
<style>
  :root{
    --brand-blue:#2b74b6;
    --brand-grey:#b2b2b2;
    --light-grey:#e6e6e6;
    --white:#ffffff;
    --stage:#2a2a2a;
  }
  *{box-sizing:border-box;margin:0;padding:0}
  html,body{width:1200px;height:852px;overflow:hidden;background:var(--stage)}
  .canvas{position:relative;width:1200px;height:852px}
  .card{position:absolute;left:280px;width:640px;height:366px;border-radius:22px;overflow:hidden}
  .card--front{top:40px;background:var(--brand-blue)}
  .card--back{top:446px;background:var(--white)}

  .logo-mark{position:absolute;border-radius:50%;background:var(--light-grey);display:flex;align-items:center;justify-content:center}
  .logo-mark__name{font-family:"Oswald",sans-serif;font-weight:600;color:var(--brand-blue);letter-spacing:2px}

  .card--front .logo-mark{width:156px;height:156px;left:242px;top:58px}
  .card--front .logo-mark__name{font-size:30px}
  .front-title{position:absolute;left:0;right:0;top:248px;text-align:center;font-family:"Oswald",sans-serif;font-weight:600;font-size:38px;letter-spacing:1px;color:var(--white)}

  .back-band{position:absolute;left:0;right:0;top:212px;bottom:0;background:var(--brand-blue)}
  .back-tab{position:absolute;left:540px;right:0;top:104px;height:120px;background:var(--brand-blue)}
  .card--back .logo-ring{position:absolute;left:460px;top:100px;width:174px;height:174px;border-radius:50%;background:var(--white)}
  .card--back .logo-mark{width:152px;height:152px;left:471px;top:111px}
  .card--back .logo-mark__name{font-size:28px}
  .back-title{position:absolute;left:60px;top:108px;font-family:"Oswald",sans-serif;font-weight:600;font-size:34px;letter-spacing:5px;color:var(--brand-blue)}

  .person{position:absolute;left:60px;top:284px;color:var(--white);font-family:"Montserrat",sans-serif}
  .person__name{font-size:24px;font-weight:500}
  .person__role{font-size:13px;opacity:.9;margin-top:2px}

  .contact{position:absolute;left:310px;top:228px;color:var(--white);font-family:"Montserrat",sans-serif;font-size:12.5px;line-height:18px}
  .contact__row{display:flex;align-items:center;gap:7px}
  .contact__row svg{width:11px;height:11px;flex:none}
  .contact__address{margin-bottom:4px}
</style>
</head>
<body>
<main class="canvas">
  <section class="card card--front">
    <div class="logo-mark"><span class="logo-mark__name">BRINDLE</span></div>
    <h1 class="front-title">BRINDLE BUILDS.</h1>
  </section>

  <section class="card card--back">
    <div class="back-band"></div>
    <div class="back-tab"></div>
    <h2 class="back-title">BRINDLE BUILDS.</h2>
    <div class="logo-ring"></div>
    <div class="logo-mark"><span class="logo-mark__name">BRINDLE</span></div>

    <div class="person">
      <p class="person__name">Marlo Fenwick</p>
      <p class="person__role">Director</p>
    </div>

    <div class="contact">
      <p class="contact__address">7c Harcourt st<br>Kingsmeadow Tas</p>
      <p class="contact__row">
        <svg viewBox="0 0 24 24"><path fill="#fff" d="M6.6 10.8a15.1 15.1 0 0 0 6.6 6.6l2.2-2.2c.3-.3.7-.4 1-.2 1.1.4 2.3.6 3.6.6.6 0 1 .4 1 1V20c0 .6-.4 1-1 1A17 17 0 0 1 3 4c0-.6.4-1 1-1h3.5c.6 0 1 .4 1 1 0 1.3.2 2.5.6 3.6.1.3 0 .7-.2 1z"/></svg>
        03 62918730
      </p>
      <p class="contact__row">
        <svg viewBox="0 0 24 24"><rect x="2" y="5" width="20" height="14" rx="2" fill="none" stroke="#fff" stroke-width="2.2"/><path d="M3 6l9 7 9-7" fill="none" stroke="#fff" stroke-width="2.2"/></svg>
        info@brindlebuilds.com.au
      </p>
      <p class="contact__row">
        <svg viewBox="0 0 24 24"><circle cx="12" cy="12" r="9.5" fill="none" stroke="#fff" stroke-width="2.2"/><path d="M2.5 12h19M12 2.5c3 3 3 16 0 19M12 2.5c-3 3-3 16 0 19" fill="none" stroke="#fff" stroke-width="1.8"/></svg>
        www.brindlebuilds.com.au
      </p>
    </div>
  </section>
</main>
</body>
</html>
```